Compelling Home Page for Clip Harbor Partners

We are a Video SEO specialist that get websites on top of the front page of Zentrova and FlickBarn with video thumbprints that generate great traffic. Video SEO is all we do

see what we're offering at a salespage www.plumfieldreels.example. However, please omit "guarantee"

he home page should introduce our company as a premier company for helping brands get their videos on the front page of zentrova and high up in flickbarn. Should incorporate video "thumbnails" as part of the design. These could be the "triangular click buttons" or little video screens you see as "thumbnails" Needs a prominent place for a video about videoSEO. on Left side of page towards the top.

Needs buttons across the top for other pages. See www.brastonclips.example for frame of reference we want to be better than them.

Must incorporate our logo. We'd like to see the logo on dark background as well as white background.

Simple but with bright and vibrant highlights that look sophisticated, cutting edge and accountable. Shows credentials. Links with examples of thumbnails that are on the front page

We want to beat www.brastonclips.example check it out for point of reference

Target Market(s)

large corporations who have videos already and want to get better traction. Marlow 500. Advertising Agencies for Marlow 500's

Requirements
Must have
• Incorporate our logo. clean, easy to read

```html
<!DOCTYPE html>
<html lang="en">
<head>
<meta charset="utf-8">
<title>Clip Harbor Partners — Experts in Video SEO</title>
<link rel="stylesheet" href="https://fonts.googleapis.com/css2?family=Ubuntu:wght@400;500;700&family=Montserrat:wght@800&family=Arimo:wght@400;700&family=Libre+Baskerville:ital@0;1&family=Tinos&display=swap">
<style>
:root{
  --ink:#111;
  --header:#050505;
  --gold-top:#d48a0c;
  --gold-1:#f6c53a;
  --gold-2:#e49a12;
  --gold-3:#d78709;
  --paper:#f1ece0;
  --quote-box:#f2e7c5;
  --quote-line:#d9cba0;
  --accent-red:#b81e0a;
  --nav-active:#f5c518;
  --muted:#555;
  --link-blue:#1f5db5;
  --btn-1:#ea5a12;
  --btn-2:#c72d08;
}
*{margin:0;padding:0;box-sizing:border-box}
html,body{width:1200px;height:1100px;overflow:hidden}
body{position:relative;background:var(--paper);font-family:Arimo,Arial,sans-serif;color:var(--ink)}
.abs{position:absolute}

.site-header{left:0;top:0;width:1200px;height:92px;background:var(--header);border-top:6px solid var(--gold-top)}
.brand{left:128px;top:13px;display:flex;align-items:center;gap:14px}
.brand-dot{width:66px;height:66px;border-radius:50%;background:var(--gold-2)}
.brand-name{font-family:Ubuntu,sans-serif;font-size:36px;font-weight:400;color:#e9e9e9;letter-spacing:-.5px}
.main-nav{top:0;left:0;font-family:Ubuntu,sans-serif;font-size:16px;color:#fff}
.main-nav a{position:absolute;top:34px;color:#fff;text-decoration:none;white-space:nowrap}
.main-nav a.active{color:var(--nav-active)}

.hero{left:0;top:92px;width:1200px;height:388px;background:radial-gradient(ellipse at 62% 40%,var(--gold-1) 0%,var(--gold-2) 55%,var(--gold-3) 100%)}
.hero-fade{left:0;top:480px;width:1200px;height:34px;background:linear-gradient(#f2c74c,var(--paper))}
.hero-video{left:110px;top:145px;width:540px;height:335px;border-radius:10px 10px 4px 4px;background:linear-gradient(#c9c9c9,#9a9a9a)}
.hero-video .screen{position:absolute;left:64px;top:16px;width:394px;height:244px;background:#000}
.hero-title{left:601px;top:156px;color:#fff;font-family:Montserrat,sans-serif;font-weight:800;line-height:1}
.hero-title .small{display:block;font-size:41px}
.hero-title .small .in{font-size:33px;margin-left:4px}
.hero-title .video{display:inline-block;font-size:60px;margin-top:-4px}
.hero-title .seo{position:absolute;left:228px;top:0;font-size:112px;letter-spacing:-2px}
.hero-sub{left:607px;top:265px;font-family:Ubuntu,sans-serif;font-weight:500;font-size:23.5px;line-height:30px;color:#141414;white-space:nowrap;letter-spacing:-.2px}
.cta{left:624px;top:345px;width:364px;height:48px;border-radius:26px;border:4px solid #f7d45a;background:linear-gradient(var(--btn-1),var(--btn-2));color:#fff;font-family:Ubuntu,sans-serif;font-weight:500;font-size:22px;display:flex;align-items:center;padding-left:22px;gap:22px}

.intro-title{left:118px;top:510px;font-family:Ubuntu,sans-serif;font-weight:700;font-size:39px;line-height:40px;letter-spacing:-.5px}
.intro-text{left:122px;top:603px;width:560px;font-size:16px;line-height:24px;color:var(--muted)}

.proof-box{left:116px;top:667px;width:588px;height:185px;background:var(--quote-box);border:1px solid var(--quote-line)}
.proof-box h3{position:absolute;left:10px;top:13px;font-family:Ubuntu,sans-serif;font-weight:500;font-size:16px}
.proof{position:absolute;font-family:"Libre Baskerville",serif;font-style:italic;font-size:14px;line-height:22px;color:#222}
.proof cite{display:block;text-align:right;font-family:Arimo,sans-serif;font-style:normal;font-weight:700;font-size:14px;color:var(--accent-red);margin-top:14px}

.section-title{font-family:Ubuntu,sans-serif;font-weight:700;font-size:23px}
.service-list{left:135px;top:910px;list-style:none;font-size:15px}
.service-list li{height:34.5px}
.service-list li::before{content:"❯";color:var(--accent-red);font-size:12px;margin-right:9px}
.client-quote{left:455px;top:920px;width:240px;font-family:Tinos,"Times New Roman",serif;font-size:17px;line-height:18px;color:#333}
.client-name{left:456px;top:991px;font-size:14px}
.client-name a{color:var(--link-blue);text-decoration:none}

.work-quote{left:773px;top:568px;width:310px;font-size:14px;line-height:18px}
.work-name{left:773px;top:659px;font-size:14px}
.work-name b{font-style:italic}
.work-name i{font-family:"Libre Baskerville",serif}
.result-shot{left:772px;top:695px;width:302px;height:267px;background:linear-gradient(#fbfbfb,#efeaf3);border:1px solid #cfcfcf}
.more-link{left:778px;top:985px;font-size:14px;color:var(--accent-red)}
.more-link span{color:#111;margin-left:10px}

.site-footer{left:0;top:1030px;width:1200px;border-top:1px solid #ddd6c6;padding:14px 0 0 136px;font-size:11px;line-height:16px;color:#666}
</style>
</head>
<body>
<header class="site-header abs">
  <div class="brand abs"><span class="brand-dot"></span><span class="brand-name">Clip Harbor Partners</span></div>
  <nav class="main-nav abs">
    <a class="active" style="left:659px">Home</a>
    <a style="left:733px">Services</a>
    <a style="left:823px">Examples</a>
    <a style="left:921px">Order</a>
    <a style="left:995px">Contact Us</a>
  </nav>
</header>

<section class="hero abs"></section>
<div class="hero-fade abs"></div>
<div class="hero-video abs" role="img" aria-label="Laptop showing the video about video SEO"><div class="screen"></div></div>
<h1 class="hero-title abs"><span class="small">Experts<span class="in">in</span></span><span class="video">VIDEO</span><span class="seo">SEO</span></h1>
<p class="hero-sub abs">We help brands get their videos on the front<br>page of zentrova and high up in flickbarn.</p>
<a class="cta abs">View Our Premier Services <svg width="26" height="22" viewBox="0 0 26 22"><path d="M3 3l8 8-8 8M13 3l8 8-8 8" fill="none" stroke="#fff" stroke-width="4"/></svg></a>

<h2 class="intro-title abs">Get your videos on the top<br>of zentrova and flickbarn.</h2>
<p class="intro-text abs">No matter what you sell or what your company size, Video Marketing is very likely your best opportunity to&nbsp; dramatically increase online sales this year</p>

<section class="proof-box abs">
  <h3>We’re not the only ones saying Video Marketing is the next big thing ...</h3>
  <blockquote class="proof" style="left:9px;top:56px;width:270px">“Videos in universal search results have a 41% higher click through rate than their plain text counterparts"<cite>Brightwell Metrics 2011 online study</cite></blockquote>
  <blockquote class="proof" style="left:310px;top:60px;width:265px">“A video result in position 4 or 5 may bet a better CTR than a a non video result in position 2 or 3"<cite>ClipSignal, 2011</cite></blockquote>
</section>

<h2 class="section-title abs" style="left:120px;top:867px">Our Core Services</h2>
<ul class="service-list abs">
  <li>Video Thumbnail Optimization</li>
  <li>Keyword Advisory Services</li>
  <li>Video production and/or enhancement</li>
</ul>

<h2 class="section-title abs" style="left:451px;top:867px">Satisfied Clients</h2>
<p class="client-quote abs">“... We now occupy 6 out of 7 of the first spots in Zentrova ... just do it before they get too busy.”</p>
<p class="client-name abs">Gareth Linwood, <a>voltcrestsupply.example</a></p>

<h2 class="section-title abs" style="left:771px;top:532px;font-size:22px">Some of our work</h2>
<p class="work-quote abs">"We were targeting a keyword with 28,600,000 competing pages in an extremely competitive market and the video was showing in position 4 within 2 weeks of being uploaded."</p>
<p class="work-name abs"><b>Martin Calloway,</b> <i>clearvettingdesk.example</i></p>
<div class="result-shot abs" role="img" aria-label="Search results page with the client video thumbnail ranked on the front page"></div>
<a class="more-link abs">view more examples <span>❯</span></a>

<footer class="site-footer abs">© Plumfield Reels.com, LLC. - All Rights Reserved<br>Trademarks on this page are the property of their respective owners.</footer>
</body>
</html>
```